The homepage of a website

This is a simple project that should take from you a few minutes as what is needed is the design of the homepage only, the details are in the attached zip file

Please note that KBLTA board required a special tailored design where they got some parts from the different posted designs, if you are interested please follow the instructions in the below URL and submit your new updated designs as per the instructions (P.S. I will mark the project as guaranteed as an assurance to all of you)

http://quorvanet.com/Projects/KBLTA/Design.jpg

Please note that KBLTA board required a special tailored design where they got some parts from the different posted designs, if you are interested please follow the instructions in the below URL and submit your new updated designs as per the instructions (P.S. I will mark the project as guaranteed as an assurance to all of you) http://quorvanet.com/Projects/KBLTA/Design.jpg

```html
<!DOCTYPE html>
<html lang="en">
<head>
<meta charset="utf-8">
<title>KBLTA — Home</title>
<link rel="stylesheet" href="https://fonts.googleapis.com/css2?family=Source+Sans+3:wght@300;400;600&family=Vollkorn:ital,wght@1,700&display=swap">
<style>
  :root{
    --page:#eceff1;
    --navy:#1b2535;
    --slate:#3a4454;
    --tan:#e3a87c;
    --menu-text:#e8b890;
    --ink:#262d3b;
    --muted:#6d7382;
    --rule:#e6e8ec;
    --orange:#f06a30;
    --sand:#d9ae8a;
    --social-dark:#2e3a48;
    --social-blue:#3b5a9a;
    --photo-top:#3d5573;
    --photo-bottom:#6a7848;
  }
  *{margin:0;padding:0;box-sizing:border-box}
  html,body{width:1200px;height:1036px;overflow:hidden}
  body{position:relative;background:var(--page);font-family:"Source Sans 3",Arial,sans-serif;color:var(--ink)}
  .abs{position:absolute}

  /* header */
  .brand{left:186px;top:20px;display:flex;align-items:center;gap:16px}
  .brand-mark{width:78px;height:78px;border-radius:50%;background:var(--navy)}
  .brand-name{font-size:40px;font-weight:600;color:var(--navy);letter-spacing:2px}

  .search{left:627px;top:17px;display:flex;height:16px}
  .search-icon{width:20px;height:16px;background:#a9adb3}
  .search-input{margin-left:6px;width:115px;height:16px;border:1px solid #c8ccd0;background:#fff;font:italic 8px Georgia,serif;color:#777;padding:3px 4px}
  .search-btn{width:43px;height:16px;background:#c9cdd1;font:italic 8px Georgia,serif;color:#f4f4f4;text-align:center;line-height:16px}
  .lang{left:836px;top:19px}
  .social{top:6px;width:32px;height:32px;border-radius:50%;background:var(--social-dark)}
  .social.blue{background:var(--social-blue)}

  .navbar{left:460px;top:64px;width:560px;height:66px;
    background:linear-gradient(90deg,rgba(27,37,53,0) 0%,rgba(60,70,88,.7) 20%,#222c3c 45%,var(--navy) 100%)}
  .nav{left:473px;top:88px;display:flex;font:italic 700 14.5px "Vollkorn",Georgia,serif;color:var(--tan);white-space:nowrap}
  .nav span.sep{margin:0 11.5px;font-weight:400;color:#b9b3ad}

  .dropdown{left:663px;top:130px;width:194px;height:158px;background:#1e2736;padding:0 25px 0 8px}
  .dropdown li{list-style:none;height:25.7px;line-height:25px;font-size:12px;color:var(--menu-text);border-bottom:1px solid #343e4e}
  .dropdown li:last-child{border-bottom:none}

  /* hero */
  .hero{left:180px;top:130px;width:840px;height:420px;background:linear-gradient(180deg,#3e4858,#333d4d 60%,#2b3444)}
  .hero-title{left:404px;top:187px;white-space:nowrap;font:700 31px Arial,Helvetica,sans-serif;color:#fff}
  .hero-sub{left:361px;top:232px;white-space:nowrap;font:700 13px Arial,Helvetica,sans-serif;color:#fff}
  .hero-photo{left:264px;top:250px;width:662px;height:300px;
    background:linear-gradient(180deg,var(--photo-top) 0%,var(--photo-bottom) 100%)}
  .hero-dropdown-layer{z-index:2}
  .arrow{top:326px}
  .dots{left:562px;top:542px;display:flex;gap:13px;align-items:center}
  .dot{width:16px;height:16px;border-radius:50%;background:#fff}
  .dot.active{width:18px;height:18px;background:#c9ecfb;box-shadow:0 0 8px 3px #a8dcf5}

  /* content */
  .content{left:180px;top:550px;width:840px;height:486px;background:#fff}
  .welcome{left:232px;top:588px}
  .welcome h1{font-size:20px;font-weight:400;color:var(--ink)}
  .welcome p{font-size:12px;color:var(--muted);margin-top:1px}
  .rule{left:180px;width:840px;height:1px;background:var(--rule)}

  .feature{top:716px;display:flex;gap:19px}
  .feature h2{font-size:20px;font-weight:400;color:var(--ink);margin-bottom:4px}
  .feature p{font-size:11px;line-height:20px;color:var(--muted);width:300px}

  .news{left:180px;top:864px;width:840px;text-align:center}
  .news h2{font-size:20px;font-weight:400;color:var(--ink)}
  .news p{font-size:12px;color:var(--muted);margin-top:1px}
  .tile{top:930px;width:223px;height:106px}
  .tile.navy{left:232px;background:var(--navy)}
  .tile.orange{left:489px;background:var(--orange)}
  .tile.sand{left:746px;background:var(--sand)}
  .pager{top:1016px;width:32px;height:32px;border-radius:50%;background:#fff;box-shadow:0 0 2px rgba(0,0,0,.08)}
</style>
</head>
<body>

<header>
  <div class="abs brand">
    <div class="brand-mark"></div>
    <div class="brand-name">KBLTA</div>
  </div>

  <div class="abs search">
    <div class="search-icon"></div>
    <div class="search-input">Resources</div>
    <div class="search-btn">Search</div>
  </div>
  <svg class="abs lang" width="22" height="11" viewBox="0 0 22 11" aria-label="English">
    <rect width="22" height="11" fill="#23367a"/>
    <rect x="9" width="4" height="11" fill="#fff"/><rect y="3.5" width="22" height="4" fill="#fff"/>
    <rect x="10" width="2" height="11" fill="#c8202f"/><rect y="4.5" width="22" height="2" fill="#c8202f"/>
  </svg>
  <a class="abs social" style="left:885px" aria-label="Social link"></a>
  <a class="abs social blue" style="left:930px" aria-label="Social link"></a>
  <a class="abs social" style="left:975px" aria-label="News feed"></a>

  <div class="abs navbar"></div>
  <nav class="abs nav">
    <span>Home</span><span class="sep">/</span>
    <span>Features</span><span class="sep">/</span>
    <span>Shortcodes</span><span class="sep">/</span>
    <span>Projects</span><span class="sep">/</span>
    <span>Blog</span><span class="sep">/</span>
    <span>Contact</span><span class="sep">/</span>
    <span>Member</span>
  </nav>
</header>

<section>
  <div class="abs hero"></div>
  <div class="abs hero-title">Lorem ipsum dolor sit amet</div>
  <div class="abs hero-sub">At vero eos et accusam et justo duo dolores et ea rebum. Stet clita kasd.</div>
  <div class="abs hero-photo" role="img" aria-label="Slide photo: landscape with trees on a grassy shore at sunset"></div>
  <svg class="abs arrow" style="left:231px" width="20" height="28" viewBox="0 0 20 28"><path d="M16 2 4 14l12 12" fill="none" stroke="#1c2433" stroke-width="5"/></svg>
  <svg class="abs arrow" style="left:950px" width="20" height="28" viewBox="0 0 20 28"><path d="M4 2l12 12L4 26" fill="none" stroke="#1c2433" stroke-width="5"/></svg>
  <div class="abs content"></div>
  <div class="abs dots"><div class="dot"></div><div class="dot active"></div><div class="dot"></div></div>

  <ul class="abs dropdown hero-dropdown-layer">
    <li>Link one</li><li>New link</li><li>Tabs</li><li>Buttons</li><li>Stuff</li><li>And so on</li>
  </ul>
</section>

<main>
  <div class="abs welcome">
    <h1>Welcome to for ‘KBLTA’ (Kingsbridge League of Tissue Arts)</h1>
    <p>Lorem ipsum dolor sit amet, consetetur sadipscing elitr, sed diam nonumy.</p>
  </div>
  <div class="abs rule" style="top:670px"></div>

  <div class="abs feature" style="left:232px">
    <svg width="32" height="28" viewBox="0 0 32 28" style="margin-top:12px"><path d="M10 1 2 6l3 7 4-2v16h14V11l4 2 3-7-8-5c-1 3-3 4-6 4s-5-1-6-4z" fill="#dbe6ee"/></svg>
    <div><h2>New Look!</h2><p>Lorem ipsum dolor sit amet, consetetur sadipscing elitr, sed diam nonumy eirmod tempor invidunt.</p></div>
  </div>
  <div class="abs feature" style="left:608px">
    <svg width="33" height="33" viewBox="0 0 32 32" style="margin-top:9px"><g fill="#d6dee5"><circle cx="16" cy="16" r="11"/><rect x="13" y="1" width="6" height="30"/><rect x="1" y="13" width="30" height="6"/><rect x="13" y="1" width="6" height="30" transform="rotate(45 16 16)"/><rect x="13" y="1" width="6" height="30" transform="rotate(-45 16 16)"/></g><circle cx="16" cy="16" r="5" fill="#fff"/></svg>
    <div><h2>Change personality</h2><p>Lorem ipsum dolor sit amet, consetetur sadipscing elitr, sed diam nonumy eirmod.</p></div>
  </div>
  <div class="abs rule" style="top:834px"></div>

  <div class="abs news">
    <h2>News and Updates</h2>
    <p>Lorem ipsum dolor sit amet, consetetur sadipscing.</p>
  </div>
  <div class="abs tile navy"></div>
  <div class="abs tile orange"></div>
  <div class="abs tile sand"></div>

  <div class="abs pager" style="left:164px"></div>
  <div class="abs pager" style="left:1004px"></div>
  <svg class="abs" style="left:174px;top:1027px" width="8" height="9" viewBox="0 0 8 9"><path d="M6 0 1 5" stroke="#b8bcc2" stroke-width="2"/></svg>
  <svg class="abs" style="left:1017px;top:1027px" width="8" height="9" viewBox="0 0 8 9"><path d="M2 0l5 5" stroke="#b8bcc2" stroke-width="2"/></svg>
</main>

</body>
</html>
```